Ridgeway Framers Business Card

I'm looking for a business card design for a start-up Handyman/Construction Company. The organization will double as a ministry to the homeless, hoping to create job opportunity and training to the homeless, providing a pathway back to being "homed". I'm looking for a simple to "seeming" simple design. Open to all thoughts.

Industry/Entity Type

Ministry

Requirements
Must have
• Logo (Attached), Name, Phone, Email and Address. Note - "*Registered and Insured".

```html
<!DOCTYPE html>
<html lang="en">
<head>
<meta charset="utf-8">
<title>Ridgeway Framers Business Card</title>
<link href="https://fonts.googleapis.com/css2?family=Montserrat:wght@400;600;700&display=swap" rel="stylesheet">
<style>
  :root {
    --backdrop: #e6e7ec;
    --navy: #242c4f;
    --ink: #2f3556;
    --purple: #7a2f8f;
    --grey: #6d6f78;
    --paper: #ffffff;
    --white: #ffffff;
  }
  * { margin: 0; padding: 0; box-sizing: border-box; }
  html, body {
    width: 1200px; height: 675px; overflow: hidden;
    background: var(--backdrop);
    font-family: "Montserrat", Arial, sans-serif;
  }
  .stage {
    width: 1200px; height: 675px;
    display: flex; align-items: center; justify-content: center; gap: 50px;
  }
  .card {
    width: 525px; height: 300px;
    position: relative;
    box-shadow: 0 6px 18px rgba(20, 24, 45, 0.18);
  }
  .card-front { background: var(--paper); }
  .card-back {
    background: var(--navy);
    display: flex; flex-direction: column; align-items: center; justify-content: center;
  }
  .brand-name {
    font-weight: 700; letter-spacing: 0.5px; line-height: 1;
  }
  .card-front .brand-name {
    position: absolute; left: 40px; top: 58px;
    font-size: 34px; color: var(--ink);
  }
  .card-front .brand-suffix {
    position: absolute; left: 236px; top: 98px;
    font-size: 10px; font-weight: 400; color: var(--ink);
  }
  .contact {
    position: absolute; left: 40px; top: 150px;
    color: var(--grey); font-size: 12.5px; line-height: 1.45;
  }
  .person { margin-bottom: 12px; font-size: 15px; }
  .person-name { color: var(--purple); font-weight: 700; }
  .person-role { color: var(--grey); font-weight: 400; margin-left: 4px; }
  .contact-line { display: flex; align-items: center; gap: 6px; }
  .contact-line svg { width: 11px; height: 11px; fill: var(--purple); flex: none; }
  .card-back .brand-name { font-size: 38px; color: var(--white); }
  .card-back .brand-suffix {
    align-self: flex-end; margin-right: 88px; margin-top: 6px;
    font-size: 10px; color: var(--white);
  }
  .credential {
    margin-top: 40px; font-size: 12px; letter-spacing: 1px; color: var(--white);
  }
</style>
</head>
<body>
  <main class="stage">
    <section class="card card-front" aria-label="Card front">
      <div class="brand-name">Ridgeway Framers</div>
      <div class="brand-suffix">Framers, LLC</div>
      <div class="contact">
        <p class="person"><span class="person-name">Dana Whitlock</span><span class="person-role">Principal</span></p>
        <p>1840 Cedar Hollow Road</p>
        <p>Fairmont, California 91020</p>
        <p class="contact-line">
          <svg viewBox="0 0 24 24" aria-hidden="true"><path d="M6.6 10.8a15.1 15.1 0 0 0 6.6 6.6l2.2-2.2c.3-.3.7-.4 1-.2 1.1.4 2.3.6 3.6.6.6 0 1 .4 1 1V20c0 .6-.4 1-1 1A17 17 0 0 1 3 4c0-.6.4-1 1-1h3.5c.6 0 1 .4 1 1 0 1.3.2 2.5.6 3.6.1.3 0 .7-.2 1z"/></svg>
          +1.555.0142786
        </p>
        <p class="contact-line">
          <svg viewBox="0 0 24 24" aria-hidden="true"><path d="M2 5h20v14H2z M2 5l10 8 10-8" fill="none" stroke="#7a2f8f" stroke-width="2.4"/></svg>
          dana@ridgewayframers.com
        </p>
      </div>
    </section>

    <section class="card card-back" aria-label="Card back">
      <div class="brand-name">Ridgeway Framers</div>
      <div class="brand-suffix">Framers, LLC</div>
      <p class="credential">Registered and Insured</p>
    </section>
  </main>
</body>
</html>
```